Business Card Design Project

We need a business card for our IT services provider business. We provide services to small and medium business, and would like something that reflects the color scheme / branding on our recently updated website - www.larkbyte.com.au

The card type we have chosen is a matte laminated double sided configuration at 86mm x 54mm on 350 GSM cardboard.
Updates

Target Market(s)

Small and Medium Business owners

Industry/Entity Type

Business

Requirements
Must have
• *Details on all cards*

Company Name: LarkByte IT Pty Ltd
ABN: 62 385 219 604
Address: 47-49 Marrow Street, Kelbrook Vale, Victoria 3150
Phone: 1300 LARK BY
Fax: 03 9417 6209
Website: www.larkbyte.com.au
Logo/Handprint Icon

*Person Specific*

```html
<!DOCTYPE html>
<html lang="en">
<head>
<meta charset="utf-8">
<title>LarkByte IT – Business Card</title>
<link rel="stylesheet" href="https://fonts.googleapis.com/css2?family=Open+Sans:wght@400;600&display=swap">
<style>
  :root {
    --stage: #d2d2d2;
    --brand-blue: #3a7aab;
    --card-white: #ffffff;
    --ink-dark: #333333;
    --ink-mid: #666666;
    --ink-light: #ffffff;
    --line-tone: rgba(255,255,255,0.10);
  }
  * { margin: 0; padding: 0; box-sizing: border-box; }
  html, body { width: 1200px; height: 900px; overflow: hidden; }
  body {
    background: var(--stage);
    font-family: "Open Sans", sans-serif;
    position: relative;
  }
  .card {
    position: absolute;
    top: 291px;
    width: 508px;
    height: 319px;
    overflow: hidden;
  }
  .card--front { left: 70px; background: var(--card-white); }
  .card--back { left: 609px; background: var(--brand-blue); color: var(--ink-light); }

  .front__tab {
    position: absolute;
    left: 0; top: 149px;
    width: 49px; height: 151px;
    background: var(--brand-blue);
    border-radius: 0 10px 10px 0;
  }
  .front__brand {
    position: absolute;
    right: 34px; top: 38px;
    display: flex; align-items: center; gap: 8px;
    font-size: 18px; font-weight: 600;
    color: var(--brand-blue);
  }
  .brand__square { width: 14px; height: 14px; background: var(--brand-blue); }
  .front__name {
    position: absolute; left: 78px; top: 155px;
    font-size: 21px; font-weight: 600; color: var(--ink-dark);
  }
  .front__role {
    position: absolute; left: 78px; top: 183px;
    font-size: 14px; color: var(--ink-mid);
  }
  .front__contacts {
    position: absolute; left: 78px; top: 227px;
    list-style: none;
    font-size: 14.5px; line-height: 20.5px; color: var(--ink-mid);
  }

  .back__pattern {
    position: absolute; right: 0; top: 0;
    width: 310px; height: 319px;
    background: linear-gradient(135deg, rgba(255,255,255,0) 0%, var(--line-tone) 50%, rgba(255,255,255,0) 100%);
  }
  .back__brand {
    position: absolute; left: 26px; top: 58px;
    display: flex; align-items: center; gap: 10px;
    font-size: 30px; font-weight: 400; color: var(--ink-light);
  }
  .brand__square--light { width: 14px; height: 14px; background: var(--ink-light); }
  .back__company {
    position: absolute; left: 83px; top: 144px;
    font-size: 13px;
  }
  .back__details {
    position: absolute; left: 25px; top: 175px;
    display: grid; grid-template-columns: 58px auto;
    font-size: 11px; line-height: 15px;
  }
  .back__details dd { margin: 0; }
  .back__gap { grid-column: 1 / 3; height: 15px; }
</style>
</head>
<body>
  <section class="card card--front">
    <div class="front__tab"></div>
    <div class="front__brand"><span class="brand__square"></span>LarkByte IT</div>
    <h1 class="front__name">Daniel Marsh</h1>
    <p class="front__role">director</p>
    <ul class="front__contacts">
      <li>(000) 000 000</li>
      <li>daniel.marsh@larkbyte.au</li>
      <li>www.larkbyte.com.au</li>
    </ul>
  </section>

  <section class="card card--back">
    <div class="back__pattern" role="img" aria-label="Faint crossing diagonal line pattern"></div>
    <div class="back__brand"><span class="brand__square--light"></span>LarkByte IT</div>
    <p class="back__company">LarkByte IT Pty Ltd</p>
    <dl class="back__details">
      <dt>ABN:</dt><dd>62 385 219 604</dd>
      <dt>address:</dt><dd>47-49 Marrow Street,<br>Kelbrook Vale,<br>Westmere 3187</dd>
      <span class="back__gap"></span>
      <dt>phone:</dt><dd>1300 LARK BY</dd>
      <dt>fax:</dt><dd>03 9417 6209</dd>
    </dl>
  </section>
</body>
</html>
```